Q spot menu

single page
we are located right across from Larkfield Grounds Gullwings ballpark
Menu has to be double sided 11”x17”

APPETIZERS
Guacamole and Chips $14 HH $9
House-made guacamole and tortilla chips. Served with pico de gallo, queso fresco and salsa.

Grand Slam Nachos $18 HH $13
House-made tortilla chips smothered with Jack and cheddar cheeses, your choice of meat (seasoned ground beef, chicken, pork carnitas, or veggies, beans, and jalapeños. Served with sour cream, guacamole, pico de gallo and salsa.

Quesadilla 15 HH$10
Flour tortilla filled with Jack and cheddar cheeses, your choice of meat (seasoned ground beef, chicken, pork carnitas, or veggies. folded in half and cooked golden brown. Served with sour cream and guacamole.

Beef Sliders $15
Premium Angus beef, Jack cheese, sauteed onions, rajas, tomato, spring mix, house mayo and chipotle aioli on a brioche bun.

Chicken Strips $15 HH $10
House-battered and breaded chicken breast strips. Served with your choice of dressing and fries. SUB ONION RINGS +$3

Corvo Wings $15 HH $10
7 Jumbo-size drums and flats tossed in your choice of sauce (BBQ, buffalo, mango habanero, or lemon pepper) or dry. Served with carrots, celery sticks, and your choice of dressing.

Onion Rings $9
Jumbo onion rings. Served with your choice of dressing.

Mozzarella Sticks $10
7 Breaded and fried mozzarella cheese sticks. Served with marinara sauce and ranch dressing.

SALADS
All salads are served with your choice of dressing (Ranch, Blue cheese, Honey mustard, or Balsamic vinaigrette).

Dinner Salad $9
Mixed greens, tomatoes, onions, cheese and carrots.

Taco Salad $17
Large flour tortilla crispy shell filled with your choice of meat (seasoned ground beef, pork carnitas, chicken or veggies, beans, lettuce, tomatoes, jalapeños and cheese. Topped with sour cream, pico de gallo and salsa.

Ahi Tuna Salad $19
Pan-seared Ahi tuna steak (6 oz.) on a bed of spring mix, tomatoes, beets, orange slices and sesame seeds.

Salmon Salad $20
Pan-seared salmon filet, on a bed of mixed greens, tomatoes, onions, avocado slices, carrots and cheese.
BURGERS ( 8oz)
Served with fries. (add an egg +$2)
El Gran Tio Burger $17
Verified Prairie Stock patty, cheddar cheese, and caramelized onions, mayo, lettuce, tomato, avocado and a fried jalapeño.

All-American Burger $16
Verified Prairie Stock patty, Cheddar cheese, mayo, lettuce, tomato, onion and pickles.
- Add bacon +$3
- Add an egg +$2

Whiskey Burger $17
Verified Prairie Stock patty, bacon, caramelized onions and Swiss cheese, mayo and house-made Moss Haverty whiskey sauce.

Mushroom Swiss Burger $17
Verified Prairie Stock patty, mayo, Swiss cheese, bacon, and mushrooms on ciabatta bread.

Veggie Burger $16 (VG)
Black bean patty on a pretzel bun with mayo, lettuce, tomato, onion, pickles, and avocado.

Salmon Burger $17
Pan-seared salmon filet (6 oz.) on a pretzel bun with mayo, lettuce, tomato, avocado and chipotle aioli.

Grilled Chicken Sandwich $16
Mayo, grilled chicken breast on ciabatta bread with lettuce, tomato, onions, pickles, and avocado.

SOUTH OF THE BORDER
3 Street Tacos 12 HH $7
seasoned ground beef, pork carnitas, chicken or veggies, pico de gallo and salsa. ADD GUAC +$3

2-lb. Burrito $15
Flour tortilla wrapped around your choice of meat seasoned ground beef, pork, chicken, or veggies. rice, beans, guacamole, sour cream, salsa and Jack and cheddar cheeses.

Chile Colorado Burrito $16
Special Trim Beef simmered in a house-made Chile Colorado sauce, rice and beans wrapped in a flour tortilla. Topped with sour cream.

EVENT MENU
Grand Slam Nachos $18
House-made tortilla chips smothered with Jack and cheddar cheeses, your choice of meat (seasoned ground beef, pork, chicken or veggies. beans and jalapeños. Served with sour cream, guacamole, pico de gallo and salsa.

3 Street Tacos $12
Your choice of meat seasoned ground beef, pork carnitas, chicken, or veggies, pico de gallo and salsa.

2-lb. Burrito $15
Flour tortilla wrapped around your choice of meat (seasoned ground beef, pork carnitas or grilled chicken) or veggies, rice, beans, guacamole, sour cream, salsa and Jack and cheddar cheeses.

Quesadilla $15
Flour tortilla filled with Jack and cheddar cheeses, your choice of meat (seasoned ground beef, pork carnitas, chicken or veggies, folded in half and cooked golden brown. Served with guacamole, pico de gallo and sour cream.

Taco Salad $17

Corvo Wings $15
7 Jumbo-size drums and flats tossed in your choice of sauce (BBQ, buffalo, mango habanero, or lemon pepper) or dry. Served with carrot and celery sticks.

Chicken Strips $15
House-battered and breaded chicken breast strips. Served with fries and your choice dressing.

All-American Burger $16
Verified Prairie Stock patty, Cheddar cheese, with mayo, lettuce, tomato, onion and pickles.
- Add bacon +$3
- Add avocado +$3

Whiskey Burger $17
Verified Prairie Stock patty, bacon, caramelized onions and Swiss cheese, with mayo and house-made Moss Haverty whiskey sauce.

Veggie Burger $16
Black bean patty, with mayo, lettuce, tomato, onion, pickles and avocado.

SIDES
basket of French fries $7
Rice $5
Beans $5
Sour cream $1
Avocado $4
Guacamole $7
Salsa 4oz. $2
Dressing $1

HOUSE SPECIALTIES
Carne Asada Entrée $23
Charbroiled skirt steak, cooked to order. Served with rice, beans, pico de gallo, salsa, sour cream, guacamole and tortillas.

Chile Colorado Entrée $18
Special Trim Beef simmered in a house-made Chile Colorado sauce. Served with rice, beans, sour cream and tortillas.

Pork Shank (Wednesdays only, until sold out) $24
Slow-baked pork shank (fork tender and fall-off-the-bone moist). Served with rice, beans, pico de gallo, salsa and tortillas. Ask your server about availability.

BEVERAGES
Soft Drinks $3.50
Zolta, Diet Zolta, Brook Fizz,
Juice $5
Orange, cranberry, pineapple, grapefruit
Milk $4

HAPPY HOUR
Mon- Fri 2-5pm & 10-Close
Any draft beer $2 off
Selected appetizers $5 off
Well drinks $2 off
Wine $2 off

Daily specials 11:30 am - 5 pm

Margarita Monday $2 off /Burgers 20%off
Tacos Tuesday $5 off /Tequila Casa Verano 1871 $19.42
Wing Wednesday $5 Off / whiskey $2 Off
Thirsty Thursday Any draft beer $5/Nachos $5 off
Emberloch Friday $6 shot /Chile colorado burrito 20%off
Saturday and Sunday Brunch 10am-1pm. Mimosas and Bloody Marrys

Please make sure that you put this note on both pages * *CONSUMING RAW OR UNDERCOOKED MEATS, POULTRY, SEAFOOD, SHELLFISH, OR EGGS MAY INCREASE YOUR RISK OF FOODBORNE ILLNESS, ESPECIALLY IF YOU HAVE CERTAIN MEDICAL CONDITIONS.

Items that have eggs or meet HAS TO BE MARKED WITH AN ASTERISK*

AUTOMATIC 20% GRATUITY ON GROUPS OF 5 OR MORE. ALL ORDERS TO GO +$1

Target Market(s)

Young crowd

Industry/Entity Type

Sports bar

Colors
FFC000
F8CF3A
FAE287
FDF2CF
FEFAEE

Requirements
Must have
• Entire menu
Nice to have
• Menu has to be simple bat VERY attractive

```html
<!DOCTYPE html>
<html lang="en">
<head>
<meta charset="utf-8">
<title>Special Menu &amp; Event Menu</title>
<link rel="stylesheet" href="https://fonts.googleapis.com/css2?family=Alegreya:ital,wght@0,400;0,700;0,800;1,400&family=Alegreya+SC:wght@700;800&family=Anton&family=Lobster&display=swap">
<style>
:root{
  --page:#f2f2f0;
  --board:#2d2d2d;
  --board-light:#3a3a3a;
  --yellow:#ffc000;
  --gold:#f8cf3a;
  --ink:#1e1e1e;
  --text:#cfcfcf;
  --text-soft:#b9b9b9;
  --menu-grey:#d9d9d9;
}
*{margin:0;padding:0;box-sizing:border-box}
html,body{width:942px;height:1200px;overflow:hidden;background:var(--page)}
body{position:relative;font-family:"Alegreya",Georgia,serif;color:var(--text)}

.card{
  position:absolute;left:68px;width:1460px;height:945px;
  transform:scale(.552);transform-origin:0 0;overflow:hidden;
  background:radial-gradient(ellipse at 50% 40%,var(--board-light),var(--board) 75%);
  box-shadow:0 6px 14px rgba(0,0,0,.35);
}
.card--special{top:66px}
.card--event{top:618px}

.title-script{position:absolute;font-family:"Lobster",cursive;color:var(--yellow);line-height:1;z-index:2;transform:rotate(-4deg)}
.title-block{position:absolute;font-family:"Anton",Impact,sans-serif;color:var(--menu-grey);line-height:1;letter-spacing:-1px}

.ribbon{position:absolute;display:flex;align-items:center;justify-content:center}
.ribbon svg{position:absolute;inset:0;width:100%;height:100%}
.ribbon h2{position:relative;font-family:"Alegreya SC",Georgia,serif;font-weight:800;color:var(--ink);font-size:27px;letter-spacing:.5px;line-height:1}

.item{position:absolute;width:410px}
.item-head{display:flex;justify-content:space-between;align-items:baseline}
.item-name{font-weight:800;color:var(--yellow);font-size:21px;line-height:1.1}
.item-name small{font-size:11px;color:var(--text)}
.price{font-weight:700;color:var(--yellow);font-size:19px;white-space:nowrap}
.price .hh{font-size:12px;margin:0 3px}
.desc{font-style:italic;font-size:11.5px;line-height:12px;color:var(--text-soft);max-width:300px;margin-top:3px}
.desc--wide{max-width:370px}
.addon{display:flex;width:255px;justify-content:space-between;font-size:12px;font-weight:700;color:var(--text);margin-top:5px;letter-spacing:.3px;line-height:14px}
.addon span+span{color:var(--yellow);font-size:10px}
.addon--tight{margin-top:1px}

.intro{position:absolute;font-style:italic;font-size:17px;line-height:18px;text-align:center;color:var(--text)}
.notice{position:absolute;text-align:center;font-size:13px;line-height:18px;letter-spacing:.6px;color:var(--text)}

.photo{position:absolute}

.badge{position:absolute;width:240px;height:190px}
.badge svg{position:absolute;inset:0;width:100%;height:100%}
.badge p{position:absolute;left:14px;top:48px;width:200px;transform:rotate(-14deg);text-align:center;font-family:"Alegreya SC",Georgia,serif;font-weight:800;color:var(--ink);font-size:14px;line-height:15px}
.badge p b{font-size:20px}

.sides{position:absolute;left:526px;top:293px;width:410px;display:grid;grid-template-columns:150px 72px 118px 70px;row-gap:10px;align-items:end;font-weight:800;font-size:21px;color:var(--text)}
.sides .p{color:var(--yellow);font-weight:700;font-size:19px}
.sides .p:nth-child(4n){text-align:right}

.happy{position:absolute;left:1016px;top:355px;width:413px;height:445px;border:2px solid var(--gold)}
.happy .when{position:absolute;left:0;width:100%;text-align:center;color:var(--gold);font-size:21px;font-weight:400}
.happy .deal{position:absolute;left:14px;right:14px;display:flex;justify-content:space-between;font-weight:800;font-size:21px;color:var(--text)}
.happy .deal span+span{color:var(--gold);font-weight:400;font-size:16px}
.daily{position:absolute;left:14px;right:14px;top:244px;display:grid;grid-template-columns:120px 72px 1fr 60px;row-gap:12px;font-size:12.5px;font-weight:800;color:var(--text);align-items:end}
.daily .v{color:var(--gold);font-weight:400;font-style:italic;font-size:13px}
.daily .v:nth-child(4n){text-align:right}
.brunch{position:absolute;left:0;width:100%;top:405px;text-align:center;font-size:16px;line-height:15px;color:var(--text)}
</style>
</head>
<body>

<section class="card card--special" aria-label="Special menu">

  <svg class="photo" style="left:0;top:0" width="480" height="240" viewBox="0 0 480 240" role="img" aria-label="Photo of loaded nachos with guacamole, pico de gallo and salsa">
    <defs><linearGradient id="nachoTone" x1="0" y1="0" x2="1" y2="1"><stop offset="0" stop-color="#9db46a"/><stop offset=".5" stop-color="#d8b46a"/><stop offset="1" stop-color="#c98a4a"/></linearGradient></defs>
    <path d="M0 0H455Q360 200 0 225Z" fill="url(#nachoTone)"/>
    <path d="M0 232Q372 212 468 0" fill="none" stroke="var(--yellow)" stroke-width="9"/>
  </svg>

  <div class="title-script" style="left:585px;top:20px;font-size:104px">Special</div>
  <div class="title-block" style="left:580px;top:86px;font-size:150px">MENU</div>

  <div class="ribbon" style="left:84px;top:258px;width:312px;height:37px">
    <svg viewBox="0 0 100 10" preserveAspectRatio="none"><polygon points="0,0 100,0 94,5 100,10 0,10 6,5" fill="var(--yellow)"/></svg>
    <h2>APPETIZERS</h2>
  </div>

  <div class="item" style="left:38px;top:318px">
    <div class="item-head"><span class="item-name">Guacamole And Chips</span><span class="price">$14<span class="hh">HH</span>$9</span></div>
    <p class="desc">House-made guacamole and tortilla chips. Served with pico de gallo, queso fresco and salsa.</p>
  </div>
  <div class="item" style="left:38px;top:382px">
    <div class="item-head"><span class="item-name">Grand Slam nachos*</span><span class="price">$18<span class="hh">HH</span>$13</span></div>
    <p class="desc">House-made tortilla chips smothered with Jack and cheddar cheeses, your choice of meat (seasoned ground beef, chicken, pork carnitas, or veggies, beans, and jalapeños. Served with sour cream, guacamole, pico de gallo and salsa.</p>
  </div>
  <div class="item" style="left:38px;top:470px">
    <div class="item-head"><span class="item-name">Quesadilla*</span><span class="price">$15<span class="hh">HH</span>$10</span></div>
    <p class="desc">Flour tortilla filled with Jack and cheddar cheeses, your choice of meat (seasoned ground beef, chicken, pork carnitas, or veggies. folded in half and cooked golden brown. Served with sour cream and guacamole.</p>
  </div>
  <div class="item" style="left:38px;top:560px">
    <div class="item-head"><span class="item-name">Beef Sliders*</span><span class="price">$15</span></div>
    <p class="desc">Premium Angus beef, Jack cheese, sauteed onions, rajas, tomato spring mix, house mayo and chipotle aioli on a brioche bun.</p>
  </div>
  <div class="item" style="left:38px;top:635px">
    <div class="item-head"><span class="item-name">Chicken Strips*</span><span class="price">$15<span class="hh">HH</span>$10</span></div>
    <p class="desc">House-battered and breaded chicken breast strips. Served with your choice of dressing and fries.</p>
    <div class="addon"><span>SUB ONION RINGS</span><span>+$3</span></div>
  </div>
  <div class="item" style="left:38px;top:722px">
    <div class="item-head"><span class="item-name">Corvo Wings*</span><span class="price">$15<span class="hh">HH</span>$10</span></div>
    <p class="desc desc--wide">7 Jumbo-size drums and flats tossed in your choice of sauce (BBQ, buffalo, mango habanero, or lemon pepper) or dry. Served with carrots, celery sticks, and your choice of dressing.</p>
  </div>
  <div class="item" style="left:38px;top:797px">
    <div class="item-head"><span class="item-name">Onion Rings</span><span class="price">$9</span></div>
    <p class="desc desc--wide">Jumbo onion rings. Served with your choice of dressing.</p>
  </div>
  <div class="item" style="left:38px;top:853px">
    <div class="item-head"><span class="item-name">Mozzarella Sticks</span><span class="price">$10</span></div>
    <p class="desc">7 Breaded and fried mozzarella cheese sticks. Served with marinara sauce and ranch dressing.</p>
  </div>

  <div class="ribbon" style="left:596px;top:248px;width:270px;height:34px">
    <svg viewBox="0 0 100 10" preserveAspectRatio="none"><polygon points="0,0 100,0 92,5 100,10 0,10 8,5" fill="var(--yellow)"/></svg>
    <h2>SALADS</h2>
  </div>
  <p class="intro" style="left:510px;top:294px;width:440px">All salads are served with your choice of dressing (Ranch, Blue cheese, Honey mustard, or Balsamic vinaigrette).</p>

  <div class="item" style="left:522px;top:345px">
    <div class="item-head"><span class="item-name">Dinner Salad</span><span class="price">$9</span></div>
    <p class="desc desc--wide">Mixed greens, tomatoes, onions, cheese and carrots.</p>
  </div>
  <div class="item" style="left:522px;top:400px">
    <div class="item-head"><span class="item-name">Taco Salad*</span><span class="price">$17</span></div>
    <p class="desc desc--wide">Large flour tortilla crispy shell filled with your choice of meat (seasoned ground beef, pork carnitas, chicken or veggies, beans, lettuce, tomatoes, jalapeños and cheese. Topped with sour cream, pico de gallo and salsa.</p>
  </div>
  <div class="item" style="left:522px;top:500px">
    <div class="item-head"><span class="item-name">Ahi Tuna Salad*</span><span class="price">$19</span></div>
    <p class="desc desc--wide">Pan-seared Ahi tuna steak (6 oz.) on a bed of spring mix, tomatoes, beets, orange slices and sesame seeds.</p>
  </div>
  <div class="item" style="left:522px;top:566px">
    <div class="item-head"><span class="item-name">Salmon Salad*</span><span class="price">$20</span></div>
    <p class="desc desc--wide">Pan-seared salmon filet, on a bed of mixed greens, tomatoes, onions, avocado slices, carrots and cheese.</p>
  </div>

  <p class="notice" style="left:505px;top:650px;width:455px">*CONSUMING RAW OR UNDERCOOKED MEATS, POULTRY, SEAFOOD, SHELLFISH, OR EGGS MAY INCREASE YOUR RISK OF FOODBORNE ILLNESS, ESPECIALLY IF YOU HAVE CERTAIN MEDICAL CONDITIONS.</p>

  <div class="badge" style="left:520px;top:735px">
    <svg viewBox="0 0 240 190">
      <polygon points="10,60 200,25 215,125 110,145 90,185 85,150 25,160" fill="var(--yellow)"/>
      <path d="M190 20L205 2M200 30L225 8L215 30L238 14" stroke="var(--menu-grey)" stroke-width="3" fill="none"/>
    </svg>
    <p>AUTOMATIC <b>20%</b><br>GRATUITY ON GROUPS OF 5<br>OR MORE<br>ALL ORDERS TO GO<br><b>+$1</b></p>
  </div>

  <svg class="photo" style="left:745px;top:725px" width="250" height="250" viewBox="0 0 250 250" role="img" aria-label="Photo of a taco salad in a crispy tortilla bowl">
    <defs><radialGradient id="tacoTone"><stop offset="0" stop-color="#e8e6d8"/><stop offset=".45" stop-color="#9bb560"/><stop offset="1" stop-color="#d6a455"/></radialGradient></defs>
    <circle cx="125" cy="125" r="118" fill="var(--yellow)"/>
    <circle cx="125" cy="125" r="108" fill="url(#tacoTone)"/>
  </svg>

  <div class="ribbon" style="left:1061px;top:40px;width:327px;height:38px">
    <svg viewBox="0 0 100 10" preserveAspectRatio="none"><polygon points="0,0 100,0 93,5 100,10 0,10 7,5" fill="var(--yellow)"/></svg>
    <h2>BURGERS ( 8oz)</h2>
  </div>
  <p class="intro" style="left:1016px;top:86px;width:410px">Served with fries. (add an egg +$2)</p>

  <div class="item" style="left:1016px;top:118px">
    <div class="item-head"><span class="item-name">El Gran Tio Burger*</span><span class="price">$17</span></div>
    <p class="desc">Verified Prairie Stock patty, cheddar cheese, and caramelized onions, mayo, lettuce, tomato, avocado and a fried jalapeño.</p>
  </div>
  <div class="item" style="left:1016px;top:182px">
    <div class="item-head"><span class="item-name">All-American Burger*</span><span class="price">$16</span></div>
    <p class="desc">Verified Prairie Stock patty, Cheddar cheese, mayo, lettuce, tomato, onion and pickles.</p>
    <div class="addon"><span>Add bacon</span><span>+$3</span></div>
    <div class="addon"><span>Add an egg</span><span>+$2</span></div>
  </div>
  <div class="item" style="left:1016px;top:290px">
    <div class="item-head"><span class="item-name">Whiskey Burger*</span><span class="price">$17</span></div>
    <p class="desc desc--wide">Verified Prairie Stock patty, bacon, caramelized onions and Swiss cheese, mayo and house-made Moss Haverty whiskey sauce.</p>
  </div>
  <div class="item" style="left:1016px;top:355px">
    <div class="item-head"><span class="item-name">Mushroom Swiss Burger*</span><span class="price">$17</span></div>
    <p class="desc">Verified Prairie Stock patty, mayo, Swiss cheese, bacon, and mushrooms on ciabatta bread.</p>
  </div>
  <div class="item" style="left:1016px;top:417px">
    <div class="item-head"><span class="item-name">Veggie Burger <small>(VG)</small></span><span class="price">$16</span></div>
    <p class="desc">Black bean patty on a pretzel bun with mayo, lettuce, tomato, onion, pickles, and avocado.</p>
  </div>
  <div class="item" style="left:1016px;top:482px">
    <div class="item-head"><span class="item-name">Salmon Burger*</span><span class="price">$17</span></div>
    <p class="desc">Pan-seared salmon filet (6 oz.) on a pretzel bun with mayo, lettuce, tomato, avocado and chipotle aioli.</p>
  </div>
  <div class="item" style="left:1016px;top:543px">
    <div class="item-head"><span class="item-name">Grilled Chicken Sandwich*</span><span class="price">$16</span></div>
    <p class="desc">Mayo, grilled chicken breast on ciabatta bread with lettuce, tomato, onions, pickles, and avocado.</p>
  </div>

  <div class="ribbon" style="left:1046px;top:625px;width:352px;height:35px">
    <svg viewBox="0 0 100 10" preserveAspectRatio="none"><polygon points="0,0 100,0 94,5 100,10 0,10 6,5" fill="var(--yellow)"/></svg>
    <h2 style="font-size:23px">SOUTH OF THE BORDER</h2>
  </div>

  <div class="item" style="left:1016px;top:678px">
    <div class="item-head"><span class="item-name">3 Street Tacos*</span><span class="price">$12<span class="hh">HH</span>$7</span></div>
    <p class="desc">seasoned ground beef, pork carnitas, chicken or veggies, pico de gallo and salsa.</p>
    <div class="addon"><span>ADD GUAC</span><span>+$3</span></div>
  </div>
  <div class="item" style="left:1016px;top:767px">
    <div class="item-head"><span class="item-name">2-lb. Burrito*</span><span class="price">$15</span></div>
    <p class="desc desc--wide">Flour tortilla wrapped around your choice of meat seasoned ground beef, pork, chicken, or veggies. rice, beans, guacamole, sour cream, salsa and Jack and cheddar cheeses.</p>
  </div>
  <div class="item" style="left:1016px;top:853px">
    <div class="item-head"><span class="item-name">Chile Colorado Burrito*</span><span class="price">$16</span></div>
    <p class="desc desc--wide">Special Trim Beef simmered in a house-made Chile Colorado sauce, rice and beans wrapped in a flour tortilla. Topped with sour cream.</p>
  </div>
</section>

<section class="card card--event" aria-label="Event menu">

  <div class="title-script" style="left:106px;top:10px;font-size:112px">Event</div>
  <div class="title-block" style="left:86px;top:86px;font-size:150px">MENU</div>

  <div class="item" style="left:38px;top:232px">
    <div class="item-head"><span class="item-name">Grand Slam Nachos*</span><span class="price">$18</span></div>
    <p class="desc desc--wide">House-made tortilla chips smothered with Jack and cheddar cheeses, your choice of meat (seasoned ground beef, pork chicken or veggies. beans and jalapeños. Served with sourcream, guacamole, pico de gallo and salsa.</p>
  </div>
  <div class="item" style="left:38px;top:314px">
    <div class="item-head"><span class="item-name">3 Street Tacos*</span><span class="price">$12</span></div>
    <p class="desc desc--wide">Your choice of meat seasoned ground beef, pork carnitas, chicken, or veggies, pico de gallo and salsa.</p>
  </div>
  <div class="item" style="left:38px;top:382px">
    <div class="item-head"><span class="item-name">2-lb. Burrito*</span><span class="price">$15</span></div>
    <p class="desc desc--wide">Flour tortilla wrapped around your choice of meat (seasoned ground beef, pork carnitas or grilled chicken) or veggies, rice, beans guacamole, sour cream, salsa and Jack and cheddar cheeses.</p>
  </div>
  <div class="item" style="left:38px;top:468px">
    <div class="item-head"><span class="item-name">Quesadilla*</span><span class="price">$15</span></div>
    <p class="desc desc--wide">Flour tortilla filled with Jack and cheddar cheeses, your choice of meat (seasoned ground beef, pork carnitas, chicken or veggies, folded in half and cooked golden brown. Served with guacamole,pico de gallo and sour cream.</p>
  </div>
  <div class="item" style="left:38px;top:545px">
    <div class="item-head"><span class="item-name">Taco Salad*</span><span class="price">$17</span></div>
    <p class="desc desc--wide">Large flour tortilla crispy shell filled with your choice of meat (seasoned ground beef, pork carnitas, chicken or veggies, beans, lettuce, tomatoes, jalapeños and cheese. Topped with sour cream pico de gallo and salsa.</p>
  </div>
  <div class="item" style="left:38px;top:625px">
    <div class="item-head"><span class="item-name">Corvo Wings*</span><span class="price">$15</span></div>
    <p class="desc desc--wide">7 Jumbo-size drums and flats tossed in your choice of sauce (BBQ, buffalo, mango habanero, or lemon pepper) or dry. Served with carrot and celery sticks.</p>
  </div>
  <div class="item" style="left:38px;top:693px">
    <div class="item-head"><span class="item-name">Chicken Strips*</span><span class="price">$15</span></div>
    <p class="desc">House-battered and breaded chicken breast strips. Served with fries and your choice dressing.</p>
  </div>

  <svg class="photo" style="left:0;top:760px" width="510" height="185" viewBox="0 0 510 185" role="img" aria-label="Photo of a bacon burger on a pretzel bun with french fries">
    <defs><linearGradient id="friesTone" x1="0" y1="0" x2="1" y2="0"><stop offset="0" stop-color="#e0b050"/><stop offset=".55" stop-color="#c8a060"/><stop offset="1" stop-color="#6b4a30"/></linearGradient></defs>
    <path d="M0 42Q300 -10 500 185H0Z" fill="url(#friesTone)"/>
    <path d="M0 34Q305 -18 510 185" fill="none" stroke="var(--yellow)" stroke-width="9"/>
  </svg>

  <div class="item" style="left:526px;top:34px">
    <div class="item-head"><span class="item-name">All-American Burger*</span><span class="price">$16</span></div>
    <p class="desc" style="margin-top:0">Verified Prairie Stock patty, Cheddar cheese, mayo, lettuce, tomato, onion and pickles.</p>
    <div class="addon" style="margin-top:3px"><span>Add bacon</span><span>+$3</span></div>
    <div class="addon addon--tight"><span>Add an egg</span><span>+$2</span></div>
  </div>
  <div class="item" style="left:526px;top:126px">
    <div class="item-head"><span class="item-name">Whiskey Burger*</span><span class="price">$17</span></div>
    <p class="desc desc--wide">Verified Prairie Stock patty, bacon, caramelized onions and Swiss cheese, mayo and house-made Moss Haverty whiskey sauce.</p>
  </div>
  <div class="item" style="left:526px;top:188px">
    <div class="item-head"><span class="item-name">Veggie Burger</span><span class="price">$16</span></div>
    <p class="desc desc--wide" style="max-width:410px">Black bean patty, with mayo, lettuce, tomato, onion, pickles and avocado.</p>
  </div>

  <div class="ribbon" style="left:590px;top:248px;width:272px;height:34px">
    <svg viewBox="0 0 100 10" preserveAspectRatio="none"><polygon points="0,0 100,0 92,5 100,10 0,10 8,5" fill="var(--yellow)"/></svg>
    <h2>SIDES</h2>
  </div>
  <div class="sides">
    <span>Basket of<br>French fries</span><span class="p">$9</span><span>Beans</span><span class="p">$9</span>
    <span>Rice</span><span class="p">$9</span><span>Avocado</span><span class="p">$4</span>
    <span>Sour cream</span><span class="p">$1</span><span>Salsa 4oz.</span><span class="p">$2</span>
    <span>Guacamole</span><span class="p">$7</span><span>Dressing</span><span class="p">$1</span>
  </div>

  <div class="ribbon" style="left:590px;top:485px;width:272px;height:35px">
    <svg viewBox="0 0 100 10" preserveAspectRatio="none"><polygon points="0,0 100,0 92,5 100,10 0,10 8,5" fill="var(--yellow)"/></svg>
    <h2>BEVERAGES</h2>
  </div>
  <div class="item" style="left:526px;top:540px;width:416px">
    <div class="item-head"><span class="item-name">Soft Drinks</span><span class="price">$3.50</span></div>
    <p class="desc">Zolta, Diet Zolta, Brook Fizz,</p>
  </div>
  <div class="item" style="left:526px;top:598px;width:416px">
    <div class="item-head"><span class="item-name">Juice</span><span class="price">$5</span></div>
    <p class="desc">Orange, cranberry, pineapple, grapefruit</p>
  </div>
  <div class="item" style="left:526px;top:653px;width:416px">
    <div class="item-head"><span class="item-name">Milk</span><span class="price">$4</span></div>
  </div>

  <div class="badge" style="left:545px;top:705px">
    <svg viewBox="0 0 240 190">
      <polygon points="10,60 200,25 215,125 110,145 90,185 85,150 25,160" fill="var(--yellow)"/>
      <path d="M190 20L205 2M200 30L225 8L215 30L238 14" stroke="var(--menu-grey)" stroke-width="3" fill="none"/>
    </svg>
    <p>AUTOMATIC <b>20%</b><br>GRATUITY ON GROUPS OF 5<br>OR MORE<br>ALL ORDERS TO GO<br><b>+$1</b></p>
  </div>

  <svg class="photo" style="left:818px;top:720px" width="190" height="205" viewBox="0 0 190 205" role="img" aria-label="Photo of a stacked burger with a fried egg and fresh vegetables">
    <defs><linearGradient id="burgerTone" x1="0" y1="0" x2="0" y2="1"><stop offset="0" stop-color="#7a3e22"/><stop offset=".45" stop-color="#e6b84a"/><stop offset=".7" stop-color="#5a3424"/><stop offset="1" stop-color="#6a9a4a"/></linearGradient></defs>
    <ellipse cx="95" cy="100" rx="88" ry="95" fill="url(#burgerTone)"/>
  </svg>

  <div class="ribbon" style="left:1036px;top:40px;width:376px;height:38px">
    <svg viewBox="0 0 100 10" preserveAspectRatio="none"><polygon points="0,0 100,0 94,5 100,10 0,10 6,5" fill="var(--yellow)"/></svg>
    <h2>HOUSE SPECIALTIES</h2>
  </div>
  <div class="item" style="left:1016px;top:92px">
    <div class="item-head"><span class="item-name">Carne Asada Entrée*</span><span class="price">$23</span></div>
    <p class="desc desc--wide">Charbroiled skirt steak, cooked to order. Served with rice, beans, pico de gallo, salsa, sour cream, guacamole and tortillas.</p>
  </div>
  <div class="item" style="left:1016px;top:162px">
    <div class="item-head"><span class="item-name">Chile Colorado Entrée*</span><span class="price">$18</span></div>
    <p class="desc desc--wide">Special Trim Beef simmered in a house-made Chile Colorado sauce. Served with rice, beans, sour cream and tortillas.</p>
  </div>
  <div class="item" style="left:1016px;top:227px">
    <div class="item-head"><span class="item-name">Pork Shank*</span><span class="price">$24</span></div>
    <p class="addon" style="width:auto;font-size:13px;margin-top:0">(Wednesdays only, until sold out)</p>
    <p class="desc desc--wide" style="margin-top:2px">Slow-baked pork shank (fork tender and fall-off-the-bone moist). Served with rice, beans, pico de gallo, salsa and tortillas. Ask your server about availability.</p>
  </div>

  <div class="happy">
    <p class="when" style="top:30px">Mon- Fri 2-5pm &amp; 10-Close</p>
    <div class="deal" style="top:66px"><span>Any draft beer</span><span>$2 off</span></div>
    <div class="deal" style="top:96px"><span>Selected appetizers</span><span>$5 off</span></div>
    <div class="deal" style="top:126px"><span>Well drinks</span><span>$5 off</span></div>
    <div class="deal" style="top:156px"><span>Wine</span><span>$2 off</span></div>
    <p class="when" style="top:198px">Daily specials 11:30 am - 5 pm</p>
    <div class="daily">
      <span>Margarita Monday</span><span class="v">$2 off</span><span>Burgers</span><span class="v">20% off</span>
      <span>Tacos Tuesday</span><span class="v">$5 off</span><span>Tequila Casa Verano 1871</span><span class="v">$19.42</span>
      <span>Wing Wednesday</span><span class="v">$5 off</span><span>Whiskey</span><span class="v">$2 off</span>
      <span>Thirsty Thursday<br>Any draft beer</span><span class="v">$5 off</span><span>Nachos</span><span class="v">$5 off</span>
      <span>Emberloch Friday</span><span class="v">$5 shot</span><span>Chile colorado burrito</span><span class="v">20% off</span>
    </div>
    <p class="brunch">Saturday and Sunday Brunch 10am-1pm<br>Mimosas and Bloody Marrys</p>
  </div>
  <div class="ribbon" style="left:1081px;top:338px;width:278px;height:37px">
    <svg viewBox="0 0 100 10" preserveAspectRatio="none"><polygon points="0,0 100,0 92,5 100,10 0,10 8,5" fill="var(--yellow)"/></svg>
    <h2>HAPPY HOUR</h2>
  </div>

  <p class="notice" style="left:1020px;top:840px;width:405px">*CONSUMING RAW OR UNDERCOOKED MEATS, POULTRY, SEAFOOD, SHELLFISH, OR EGGS MAY INCREASE YOUR RISK OF FOODBORNE ILLNESS, ESPECIALLY IF YOU HAVE CERTAIN MEDICAL CONDITIONS.</p>
</section>

</body>
</html>
```